Looking for a Lumora Book Cover

My book has been online for a while and I am now looking for a professional cover for it as it has been very well received.

You can view the book here and all the details about it:

https://www.pagevaultshop.example/dp/X7Q2KRMTPL#readerNotes

Not sure what I am looking for as a design, just open to your ideas.

I want something different that will stand out please.

Thanks
Owen

```html
<!DOCTYPE html>
<html lang="en">
<head>
<meta charset="utf-8">
<title>Roots and Resilience — Cover</title>
<link href="https://fonts.googleapis.com/css2?family=Big+Shoulders+Display:wght@600;700&family=Oswald:wght@400;500;600&display=swap" rel="stylesheet">
<style>
  :root {
    --ink: #000000;
    --accent: #00f2f5;
    --paper: #f2f2f2;
    --canvas-w: 778px;
    --canvas-h: 1200px;
  }
  * { margin: 0; padding: 0; box-sizing: border-box; }
  html, body {
    width: var(--canvas-w);
    height: var(--canvas-h);
    overflow: hidden;
    background: var(--ink);
  }
  .cover {
    position: relative;
    width: var(--canvas-w);
    height: var(--canvas-h);
    background: var(--ink);
    overflow: hidden;
  }
  .tagline {
    position: absolute;
    left: 0;
    width: 100%;
    text-align: center;
    font-family: "Oswald", sans-serif;
    font-variant: small-caps;
    line-height: 1;
    white-space: nowrap;
  }
  .tagline--primary {
    top: 70px;
    color: var(--paper);
    font-weight: 500;
    font-size: 27px;
    letter-spacing: 3px;
  }
  .tagline--primary span { display: block; height: 42px; }
  .tagline--secondary {
    top: 180px;
    color: var(--accent);
    font-weight: 500;
    font-size: 26px;
    letter-spacing: 3.4px;
  }
  .tagline--secondary span { display: block; height: 35px; }
  .rule {
    position: absolute;
    left: 0;
    width: 100%;
    height: 2px;
    background: var(--accent);
  }
  .rule--top { top: 310px; }
  .rule--bottom { top: 1019px; }
  .portrait {
    position: absolute;
    left: 300px;
    top: 360px;
    width: 200px;
    height: 600px;
    background: radial-gradient(ellipse at 70% 45%, rgba(0,242,245,0.18) 0%, rgba(0,242,245,0.05) 55%, rgba(0,0,0,0) 80%);
  }
  .title {
    position: absolute;
    left: 200px;
    top: 466px;
    font-family: "Big Shoulders Display", sans-serif;
    font-weight: 700;
    color: var(--paper);
    line-height: 1;
    white-space: nowrap;
    transform: scaleX(0.65);
    transform-origin: left top;
  }
  .title__line {
    display: block;
    font-size: 128px;
    letter-spacing: 15px;
    height: 118px;
    text-transform: uppercase;
  }
  .title__initial { color: var(--accent); }
  .title__line--outline {
    color: transparent;
    -webkit-text-stroke: 2.5px var(--accent);
    letter-spacing: 14px;
  }
  .author {
    position: absolute;
    left: 0;
    top: 1092px;
    width: 100%;
    text-align: center;
    font-family: "Oswald", sans-serif;
    font-weight: 600;
    font-size: 26px;
    letter-spacing: 11.5px;
    color: var(--paper);
    text-transform: uppercase;
    white-space: nowrap;
  }
</style>
</head>
<body>
  <main class="cover">
    <p class="tagline tagline--primary">
      <span>A Celebration Of Culture</span>
      <span>Struggle And Achievemen</span>
    </p>
    <p class="tagline tagline--secondary">
      <span>The History, Resistance and Excellence of</span>
      <span>Black People inAfrica and the Diaspora</span>
    </p>

    <div class="rule rule--top"></div>

    <div class="portrait" role="img" aria-label="Cyan line-art profile illustration of a person with a rising sprout below"></div>

    <h1 class="title">
      <span class="title__line"><span class="title__initial">R</span>oots</span>
      <span class="title__line title__line--outline">And</span>
      <span class="title__line"><span class="title__initial">R</span>esilience</span>
    </h1>

    <div class="rule rule--bottom"></div>

    <p class="author">Darius Whitfield</p>
  </main>
</body>
</html>
```